Website for Prestigious Trailers and Floats

Design a prestigious website, to be used on mobile phones, and computers.
Must be able to be edited by myself
Please refer to www.marrowbeckhaulage.com.au
Needs to focus on the "Marrowbeck Trailers"" name, and the "Dunmere Ashby Trailers" name.
Three trailer types to be highlighted are QX408/QX412 Horse Floats, RV3072 /RV81 Trailers, and LP5840/5296 Tipper Trailers
Needs Home Page,
Home page to include highlighted trailer types, slider for testimonials, Phone number, location, social media links, blog/news spot
Page for each of the highlighted trailer types/variations on the model
Page for multiple other trailer types

Logo's attached, can be broken up and used in parts if necessary for design

Target Market(s)

Western Australia, Horse People, Commercial Trailer Users, Handymen, Mini Digger Users, Tradesmen

Industry/Entity Type

Mining, Commercial, Government, Trades, Industry, Hobbyist

Coding

Coded - Design and coding required

Number of Pages Required

5+ page

Requirements
Must have
• See brief above
Nice to have
• See brief above

```html
<!DOCTYPE html>
<html lang="en">
<head>
<meta charset="utf-8">
<title>Marrowbeck Trailers</title>
<link href="https://fonts.googleapis.com/css2?family=Roboto:wght@400;500;700;900&family=Arimo:wght@400;700&display=swap" rel="stylesheet">
<style>
:root{
  --orange:#f05a28;
  --dark:#1b1b1b;
  --ink:#222;
  --muted:#8a8a8a;
  --light:#f0f0f0;
  --white:#fff;
  --line:#e6e6e6;
}
*{box-sizing:border-box;margin:0;padding:0}
html,body{width:1200px;height:5302px;overflow:hidden}
body{position:relative;background:var(--light);font-family:"Arimo",Arial,sans-serif;color:var(--ink)}
.abs{position:absolute}
.head{font-family:"Roboto",Arial,sans-serif;font-weight:700}
.btn{display:inline-block;background:var(--orange);color:var(--white);font-family:"Roboto",sans-serif;font-weight:500;font-size:11px;letter-spacing:1px;text-transform:uppercase;text-align:center}
.photo{position:absolute}
/* nav */
.nav{position:absolute;left:0;top:0;width:1200px;height:86px;background:var(--white)}
.brand{position:absolute;left:58px;top:30px;display:flex;align-items:center;gap:8px;font-family:"Roboto",sans-serif;font-weight:700;font-size:16px;color:var(--ink)}
.brand i{width:16px;height:16px;background:var(--orange);display:block}
.menu{position:absolute;left:384px;top:38px;display:flex;gap:38px;font-family:"Roboto",sans-serif;font-size:11px;font-weight:500;letter-spacing:1px}
.menu .on{color:var(--orange)}
.nav .btn{position:absolute;left:937px;top:25px;width:162px;height:38px;line-height:38px}
/* hero */
.hero{left:0;top:86px;width:1200px;height:676px;background:linear-gradient(160deg,#2b2f3d 0%,#4a3e32 45%,#6b5744 100%);clip-path:polygon(0 0,100% 0,100% 604px,560px 676px,0 624px)}
.hero-title{left:70px;top:238px;font-size:44px;line-height:52px;color:var(--white);font-family:"Roboto",sans-serif;font-weight:900}
.hero-title span{color:var(--orange)}
.hero-text{left:70px;top:484px;width:470px;font-size:14.5px;line-height:24px;color:var(--white)}
.play{left:818px;top:362px;width:60px;height:60px;border-radius:50%;background:var(--orange)}
/* types */
.sec-title{font-size:38px;color:var(--ink);font-family:"Roboto",sans-serif;font-weight:700}
.type{position:absolute;top:960px;width:258px;height:296px}
.type .photo{left:0;top:0;width:258px;height:190px;background:linear-gradient(#fff,#e3e3e3)}
.type .box{position:absolute;left:10px;top:148px;width:238px;height:148px;background:var(--white);box-shadow:0 2px 8px rgba(0,0,0,.08);text-align:center}
.type h3{font-family:"Roboto",sans-serif;font-weight:500;font-size:16px;margin-top:36px}
.type .btn{width:102px;height:38px;line-height:38px;font-size:13px;letter-spacing:0;text-transform:none;margin-top:22px}
/* about */
.about-card{left:551px;top:1416px;width:584px;height:388px;background:var(--white);box-shadow:0 2px 12px rgba(0,0,0,.07);padding:58px 58px}
.eyebrow{font-family:"Roboto",sans-serif;font-size:11px;letter-spacing:1.5px;color:var(--orange);font-weight:500}
.about-card h2{font-size:40px;line-height:44px;margin:16px 0 18px}
.body{font-size:12.5px;line-height:21px;color:var(--muted)}
.link{font-family:"Roboto",sans-serif;font-size:11px;letter-spacing:1px;color:#444}
/* featured */
.featured{left:0;top:2043px;width:1200px;height:660px;background:var(--white)}
.fcard{position:absolute;top:2188px;width:252px;height:462px;background:var(--white);box-shadow:0 2px 10px rgba(0,0,0,.09);padding:0 28px}
.fcard .photo{position:relative;width:196px;height:150px;margin-top:20px;background:linear-gradient(#fff,#e6e6e6)}
.fcard h4{font-family:"Roboto",sans-serif;font-weight:700;font-size:15px;margin:34px 0 34px}
.spec{display:flex;gap:14px;font-size:12.5px;line-height:18px;color:var(--muted);margin-bottom:9px}
.spec i{flex:none;width:13px;height:11px;background:var(--orange);border-radius:2px;margin-top:3px}
.fcard .btn{width:144px;height:36px;line-height:36px;margin-top:24px}
/* quality */
.feat{position:absolute;width:280px}
.feat svg{position:absolute;left:0;top:0}
.feat h5{margin-left:62px;font-family:"Roboto",sans-serif;font-weight:500;font-size:19px}
.feat p{margin-left:62px;margin-top:10px;font-size:12.5px;line-height:21px;color:var(--muted)}
/* testimonials */
.tband{left:0;top:3495px;width:1200px;height:398px;background:linear-gradient(180deg,#3a3c3f,#26282b)}
.tcard{position:absolute;top:3778px;height:250px;background:var(--white);box-shadow:0 2px 12px rgba(0,0,0,.08);padding:34px 30px}
.tcard p{font-size:12.5px;line-height:21px;color:var(--muted)}
.stars{color:var(--orange);font-size:18px;letter-spacing:2px;margin:24px 0 10px}
.who{display:flex;align-items:center;gap:18px}
.who i{width:56px;height:56px;border-radius:50%;background:#c7b8ad;display:block}
.who b{font-family:"Roboto",sans-serif;font-weight:500;font-size:15px;display:block}
.who span{font-size:11.5px;color:#b5b5b5}
/* news */
.ncard{position:absolute;top:4218px;width:344px;height:490px;background:var(--white);box-shadow:0 2px 10px rgba(0,0,0,.07)}
.ncard .photo{position:relative;height:280px;background:linear-gradient(160deg,#9aa0a0,#d7d8d5 55%,#b7bab8)}
.ncard h4{font-family:"Roboto",sans-serif;font-weight:500;font-size:21px;margin:32px 28px 18px}
.ncard .date{margin:0 28px;font-size:12px;color:#b8b8b8}
.ncard p{margin:20px 28px 0;font-size:12.5px;line-height:21px;color:var(--muted)}
/* contact & footer */
.footer{left:0;top:4876px;width:1200px;height:426px;background:var(--dark)}
.cbar{left:19px;top:4798px;width:1162px;height:123px;background:#252525}
.citem{position:absolute;top:4845px;display:flex;gap:18px;color:var(--white)}
.citem b{font-family:"Roboto",sans-serif;font-weight:500;font-size:20px;display:block}
.citem span{font-size:12px}
.fcol{position:absolute;top:4978px;color:var(--white)}
.fcol h6{font-family:"Roboto",sans-serif;font-weight:500;font-size:19px;margin-bottom:22px}
.fcol li{list-style:none;font-size:12.5px;line-height:29px}
.fcol li:before{content:"›";color:var(--orange);font-weight:700;margin-right:14px}
.soc{display:inline-block;width:28px;height:28px;background:var(--orange);margin-right:10px}
.copy{left:66px;top:5260px;font-size:12px;color:var(--white)}
.pay{position:absolute;top:5258px;width:22px;height:15px;background:#dcdcdc;border-radius:2px}
</style>
</head>
<body>

<header class="nav">
  <div class="brand"><i></i>Marrowbeck</div>
  <nav class="menu"><span class="on">HOME</span><span>ABOUT</span><span>TRAILERS</span><span>BLOG</span><span>CONTACT US</span></nav>
  <span class="btn">Browse Trailers</span>
</header>

<section class="abs hero" role="img" aria-label="Photo of a tipper trailer being loaded on a rocky quarry site, worker in hi-vis"></section>
<h1 class="abs hero-title">We Pride Ourselves<br>On Supplying Well<br><span>Designed &amp;<br>Engineered Trailers.</span></h1>
<p class="abs hero-text">Lorem ipsum dolor sit amet consectetur adipiscing elit. Utelit tellus luctus nec ullamcorper mattis pulvinar dapibus.</p>
<div class="abs play"><svg width="60" height="60"><path d="M26 21 L39 30 L26 39Z" fill="#fff"/></svg></div>

<h2 class="abs sec-title" style="left:0;width:1124px;text-align:center;top:848px">Trailer Types</h2>
<div class="type" style="left:66px"><div class="photo" role="img" aria-label="Tipper trailer photo"></div><div class="box"><h3>Tipper Trailers</h3><span class="btn">Browse</span></div></div>
<div class="type" style="left:333px"><div class="photo" role="img" aria-label="Horse float photo"></div><div class="box"><h3>Horse Floats</h3><span class="btn">Browse</span></div></div>
<div class="type" style="left:600px"><div class="photo" role="img" aria-label="Cage trailer photo"></div><div class="box"><h3>Dunmere Ashby</h3><span class="btn">Browse</span></div></div>
<div class="type" style="left:867px"><div class="photo" role="img" aria-label="Raised tipper trailer photo"></div><div class="box"><h3>Marrowbeck</h3><span class="btn">Browse</span></div></div>

<div class="photo" style="left:10px;top:1378px;width:580px;height:562px;background:linear-gradient(#d8d8d8,#bdbdbd)" role="img" aria-label="Tipper trailer with raised cage bed in a showroom"></div>
<div class="abs about-card">
  <div class="eyebrow">ABOUT US</div>
  <h2 class="head">We Provide Trailers With High Quality</h2>
  <p class="body">Lorem ipsum dolor sit amet, consectetur adipiscing elit. Doneca feugiat purus. Duis turpis nunc aliquam id nunc acconvallis dictum nisi. Curabitur vehicula tincidunt sapien velcac. Donec diam augue consequat sit amet metus acbibendum mattis massauis mollis ligula pretium consequat.</p>
  <div style="display:flex;align-items:center;gap:36px;margin-top:24px">
    <span class="btn" style="width:128px;height:38px;line-height:38px">Read More</span>
    <span class="link">BROWSE TRAILERS &nbsp;⟶</span>
  </div>
</div>

<section class="abs featured"></section>
<h2 class="abs head" style="left:56px;top:2110px;font-size:34px">Featured Trailers</h2>
<span class="abs btn" style="left:972px;top:2114px;width:172px;height:38px;line-height:38px">View All Trailers</span>

<div class="fcard" style="left:56px"><div class="photo" role="img" aria-label="Cage trailer product photo"></div><h4>LP5840</h4>
  <div class="spec"><i></i>Model :MB2204 ( 8' x 5' )<br>(Manual)</div><div class="spec"><i></i>Tyre : 195/60/12</div><div class="spec"><i></i>Weight : 2700kg</div><div class="spec"><i></i>Internal Length : 2.46m / 8'</div><span class="btn">More Details</span></div>
<div class="fcard" style="left:328px"><div class="photo" role="img" aria-label="Tipper trailer product photo" style="margin-top:12px"></div><h4 style="margin-top:30px">LP5840</h4>
  <div class="spec"><i></i>Model :MB2204 ( 8' x 5' )<br>(Manual)</div><div class="spec"><i></i>Tyre : 195/60/12</div><div class="spec"><i></i>Weight : 2700kg</div><div class="spec"><i></i>Internal Length : 2.46m / 8'</div><span class="btn">More Details</span></div>
<div class="fcard" style="left:600px"><div class="photo" role="img" aria-label="Horse float product photo" style="margin-top:16px"></div><h4 style="margin-top:32px">QX408</h4>
  <div class="spec"><i></i>Model :MB2204 ( 8' x 5' )<br>(Manual)</div><div class="spec"><i></i>Tyre : 195/60/12</div><div class="spec"><i></i>Weight : 2700kg</div><div class="spec"><i></i>Internal Length : 2.46m / 8'</div><span class="btn">More Details</span></div>
<div class="fcard" style="left:872px"><div class="photo" role="img" aria-label="Cage trailer product photo"></div><h4>LP5840</h4>
  <div class="spec"><i></i>Model :MB2204 ( 8' x 5' )<br>(Manual)</div><div class="spec"><i></i>Tyre : 195/60/12</div><div class="spec"><i></i>Weight : 2700kg</div><div class="spec"><i></i>Internal Length : 2.46m / 8'</div><span class="btn">More Details</span></div>

<div class="abs" style="left:70px;top:2920px;width:30px;height:452px;background:var(--orange)"></div>
<div class="photo" style="left:97px;top:2858px;width:406px;height:514px;background:linear-gradient(#dcdcdc,#b9b9b9)" role="img" aria-label="Tipper trailer with raised cage bed"></div>
<h2 class="abs head" style="left:608px;top:2866px;font-size:40px;line-height:44px;width:540px">Quality Trailers + Floats for Sale</h2>
<p class="abs body" style="left:608px;top:2972px;width:560px">Lorem ipsum dolor sit amet, consectetur adipiscing elit. Doneca feugiat purus. Duis turpis nunc aliquam id nunc acconvallis dictum nisi. Curabitur vehicula tincidunt sapien velcac. Donec diam augue consequat sit amet metus acbibendum mattis.</p>
<div class="feat" style="left:608px;top:3054px"><svg width="40" height="40" fill="none" stroke="#f05a28" stroke-width="2"><circle cx="20" cy="12" r="8"/><path d="M4 34 h10 l6-4 h12"/></svg><h5>Competitive Pricing</h5><p>Lorem ipsum dolor sit amet consec tetur adipiscing elit pretium sollicitudin.</p></div>
<div class="feat" style="left:908px;top:3054px"><svg width="40" height="40" fill="none" stroke="#f05a28" stroke-width="2"><circle cx="20" cy="20" r="16"/><path d="M12 20 l6 6 l10-12"/></svg><h5>Trusted Service</h5><p>Lorem ipsum dolor sit amet consec tetur adipiscing elit pretium sollicitudin.</p></div>
<div class="feat" style="left:608px;top:3196px"><svg width="40" height="40" fill="none" stroke="#f05a28" stroke-width="2"><path d="M6 34 L34 6 M6 6 L34 34"/></svg><h5>Breakdown Assistance</h5><p>Lorem ipsum dolor sit amet consec tetur adipiscing elit pretium sollicitudin.</p></div>
<div class="feat" style="left:908px;top:3196px"><svg width="40" height="40" fill="none" stroke="#f05a28" stroke-width="2"><path d="M6 22 a14 14 0 0 1 28 0"/><rect x="4" y="22" width="6" height="10"/><rect x="30" y="22" width="6" height="10"/></svg><h5>24/7 Support</h5><p>Lorem ipsum dolor sit amet consec tetur adipiscing elit pretium sollicitudin.</p></div>

<section class="abs tband" role="img" aria-label="Dark photo of trailers inside a workshop"></section>
<div class="abs eyebrow" style="left:0;width:1200px;text-align:center;top:3602px">TESTIMONIAL</div>
<h2 class="abs head" style="left:0;width:1200px;text-align:center;top:3624px;font-size:40px;color:#fff">What Our Clients Say</h2>
<p class="abs" style="left:240px;width:720px;text-align:center;top:3688px;font-size:12.5px;line-height:21px;color:#fff">Lorem ipsum dolor sit amet, consectetur adipiscing elit, sed do eius tempor incididunt ut labore et dolore magna aliqua. Adqua minim veniam quis exercitation incididunt magna aliqua veniam quis.</p>
<div class="tcard" style="left:62px;width:332px"><p>Lorem ipsum dolor sit amet, consectetur adip iscing elit, sed do eiusmod tempor incididunt ut labore et dolore magna aliqua.</p><div class="stars">★★★★★</div><div class="who"><i></i><div><b>Owen Carlisle</b><span>Project Manager</span></div></div></div>
<div class="tcard" style="left:430px;width:338px"><p>Lorem ipsum dolor sit amet, consectetur adip iscing elit, sed do eiusmod tempor incididunt ut labore et dolore magna aliqua.</p><div class="stars">★★★★½</div><div class="who"><i></i><div><b>Maya Thornbury</b><span>Marketing Staff</span></div></div></div>
<div class="tcard" style="left:804px;width:339px"><p>Lorem ipsum dolor sit amet, consectetur adip iscing elit, sed do eiusmod tempor incididunt ut labore et dolore magna aliqua.</p><div class="stars">★★★★★</div><div class="who"><i></i><div><b>Lachlan Pryce</b><span>IT Programmer</span></div></div></div>

<div class="abs eyebrow" style="left:56px;top:4124px">OUR NEWS</div>
<h2 class="abs head" style="left:56px;top:4144px;font-size:38px">Latest News</h2>
<span class="abs btn" style="left:996px;top:4158px;width:148px;height:36px;line-height:36px">View All News</span>
<div class="ncard" style="left:56px"><div class="photo" role="img" aria-label="Aerial photo of workers on a concrete site"></div><h4>Tipper Trailers everywhere!</h4><div class="date">▢ &nbsp;October 22, 2023</div><p>These tipper trailers are being hired out by builders, contractors, landscapers and DIYers, making that job of...</p></div>
<div class="ncard" style="left:428px"><div class="photo" role="img" aria-label="Aerial photo of workers on a concrete site"></div><h4>Tipper Trailers everywhere!</h4><div class="date">▢ &nbsp;October 22, 2023</div><p>These tipper trailers are being hired out by builders, contractors, landscapers and DIYers, making that job of...</p></div>
<div class="ncard" style="left:800px"><div class="photo" role="img" aria-label="Aerial photo of workers on a concrete site"></div><h4>Tipper Trailers everywhere!</h4><div class="date">▢ &nbsp;October 22, 2023</div><p>These tipper trailers are being hired out by builders, contractors, landscapers and DIYers, making that job of...</p></div>

<footer class="abs footer"></footer>
<div class="abs cbar"></div>
<div class="citem" style="left:80px"><svg width="28" height="28"><path d="M6 3 l6 0 2 7-4 3 a16 16 0 0 0 6 6 l3-4 7 2 0 6 a3 3 0 0 1-3 3 C13 26 2 15 3 6 a3 3 0 0 1 3-3z" fill="#f05a28"/></svg><div><b>Call Us</b><span>+(08) 9400-1275</span></div></div>
<div class="citem" style="left:368px"><svg width="28" height="28"><rect x="2" y="7" width="24" height="16" fill="#f05a28"/><path d="M2 7 l12 9 12-9" stroke="#252525" stroke-width="2" fill="none"/></svg><div><b>Email Us</b><span>hello@marrowbeck.example</span></div></div>
<div class="citem" style="left:642px"><svg width="28" height="28"><path d="M14 2 a9 9 0 0 1 9 9 c0 7-9 15-9 15 s-9-8-9-15 a9 9 0 0 1 9-9z" fill="#f05a28"/><circle cx="14" cy="11" r="3" fill="#252525"/></svg><div><b>Our Location</b><span>Harlow Road 42, Kalgoorlie</span></div></div>
<div class="citem" style="left:950px"><svg width="28" height="28"><circle cx="14" cy="14" r="11" fill="#f05a28"/><path d="M14 8 v7 h5" stroke="#252525" stroke-width="2" fill="none"/></svg><div><b>Work Hours</b><span>09:00 AM - 22:00 PM</span></div></div>

<div class="abs brand" style="left:66px;top:4976px;color:#fff"><i></i>Marrowbeck</div>
<p class="abs" style="left:66px;top:5018px;width:280px;font-size:12px;line-height:20px;color:#fff">Lorem ipsum dolor sit amet, consectetur adipiscing elit, sed do eiusmod tempor incididunt ut labore et dolore eiusmod tempor.</p>
<div class="fcol" style="left:393px"><h6>Quick Links</h6><ul><li>About</li><li>Rent</li><li>Reservation</li><li>Team</li><li>Contact</li></ul></div>
<div class="fcol" style="left:608px"><h6>Useful Links</h6><ul><li>Privacy Policy</li><li>Terms and Conditions</li><li>Disclaimer</li><li>Support</li><li>FAQ</li></ul></div>
<div class="fcol" style="left:852px"><h6>Follow Us</h6><span class="soc"></span><span class="soc"></span><span class="soc"></span><span class="soc"></span></div>
<div class="abs" style="left:19px;top:5232px;width:1162px;height:1px;background:#333"></div>
<p class="abs copy">Copyright © 2021 Marrowbeck Trailers. All rights reserved.</p>
<span class="pay" style="left:964px"></span><span class="pay" style="left:1000px"></span><span class="pay" style="left:1036px"></span><span class="pay" style="left:1072px"></span><span class="pay" style="left:1108px"></span>

</body>
</html>
```